Epoxy Flooring Contractor business card

We need a business card to promote a new addition to our business. We now offer Epoxy Flooring. We would like for the business card to include the images attached. One is our logo, the other is a sample of metallic epoxy flooring, we would like to incorporate that somewhere into the design. I was thinking an icon of a man pushing a concrete grinder and have the color set to the metallic epoxy color. I found a business card sample on this website, I will attach it. It has the icon that we are looking for, or something similar.
Our company name is Harborline Coatings LLC
Our owners name is Dane Morrow
Phone is 561-482-7160
website is www.harborline-coatingsllc.example
please let me know if you need any other info

Contact Information for Business Card

Harborline Coatings LLC
Dane Morrow, owner
Phone: 561-482-7160
Address: P.O Box 8241 Lake Worth, FL 33467
www.Harborline-CoatingsLLC.example
HarborlineCoatingsLLC@mailbox.example
Include logo attached
It must include a Clip art of man with concrete grinder
Must include metallic epoxy design attached
Must include the following text
Residential Garage Flooring
Epoxy Countertops
Commercial Epoxy Flooring
Restaurant Flooring
Warehouse Flooring
Licensed & Insured
Free Estimates

Colors

Designer to choose colors to be used in the design.

Requirements
Must have
• Include logo attached
• It must include a Clip art of man with concrete grinder
• Must include metallic epoxy design attached
• Must include the following text
• Garage Epoxy Flooring
• Residential Epoxy Flooring
• Concrete Floor Crack Repairs
• Concrete Floor Grinding
• Commercial & Warehouse Epoxy Flooring
• Restaurant Epoxy Flooring
• Epoxy Countertops
• Non Slip Epoxy Pool Decks
• Textured Finishes, Flakes, Granite Coat, Metallic & Quartz
• FREE ESTIMATES • LICENSED & INSURED

```html
<!DOCTYPE html>
<html lang="en">
<head>
<meta charset="utf-8">
<title>Harborline Coatings – Business Card</title>
<link rel="stylesheet" href="https://fonts.googleapis.com/css2?family=Open+Sans:wght@400;600;700&display=swap">
<style>
  :root {
    --stage: #2c2c2c;
    --paper: #ffffff;
    --brand-blue: #2f5b8c;
    --slate-blue: #4a6c96;
    --light-blue: #7ea6d6;
    --ink-grey: #5a5a5a;
    --rule-grey: #d2d2d2;
    --faint-mark: #f1f1f1;
    --epoxy-deep: #27508a;
    --epoxy-mid: #4b7bb8;
    --epoxy-light: #9bbbe0;
  }
  * { box-sizing: border-box; margin: 0; padding: 0; }
  html, body { width: 1200px; height: 866px; overflow: hidden; }
  body {
    background: var(--stage);
    font-family: "Open Sans", sans-serif;
    display: flex; flex-direction: column; align-items: center; justify-content: center;
    gap: 30px;
  }
  .card {
    position: relative; width: 700px; height: 400px; overflow: hidden;
    box-shadow: 0 10px 24px rgba(0,0,0,.45);
  }

  /* Front */
  .card-front { background: var(--paper); }
  .backdrop-mark {
    position: absolute; left: 150px; top: 20px; width: 250px; height: 250px;
    background: var(--faint-mark);
  }
  .holder { position: absolute; left: 50px; top: 80px; }
  .holder-name { font-size: 32px; font-weight: 700; color: var(--brand-blue); line-height: 1.1; }
  .holder-role { font-size: 16px; color: var(--ink-grey); }
  .contact-list { position: absolute; left: 50px; top: 160px; list-style: none; }
  .contact-list li {
    display: flex; align-items: center; gap: 8px;
    font-size: 15px; color: var(--ink-grey); line-height: 25px;
  }
  .contact-list svg { width: 14px; height: 14px; fill: var(--brand-blue); flex: none; }
  .divider { position: absolute; left: 50px; right: 50px; top: 260px; height: 1px; background: var(--rule-grey); }
  .brand-slot {
    position: absolute; right: 50px; top: 150px;
    display: flex; align-items: center; gap: 12px;
  }
  .brand-square { width: 44px; height: 44px; background: var(--brand-blue); flex: none; }
  .brand-name {
    font-size: 26px; font-weight: 600; color: var(--ink-grey); line-height: 1.05;
  }
  .company { position: absolute; right: 50px; top: 282px; text-align: right; }
  .company-name { font-size: 17px; font-weight: 700; color: var(--brand-blue); }
  .company-address { font-size: 15px; color: var(--ink-grey); line-height: 1.35; }
  .edge-band { position: absolute; left: 0; right: 0; bottom: 0; height: 12px; background: var(--light-blue); }
  .edge-band::after {
    content: ""; position: absolute; right: 0; top: 0; bottom: 0; width: 48%;
    background: var(--brand-blue);
  }

  /* Back */
  .card-back { background: var(--slate-blue); }
  .epoxy-texture {
    position: absolute; inset: 0 0 0 30%;
    background:
      radial-gradient(circle at 30% 70%, var(--epoxy-light) 0, transparent 22%),
      radial-gradient(circle at 75% 30%, var(--epoxy-light) 0, transparent 25%),
      radial-gradient(circle at 60% 85%, var(--epoxy-mid) 0, transparent 30%),
      linear-gradient(135deg, var(--epoxy-mid), var(--epoxy-deep));
    -webkit-mask-image: linear-gradient(to right, transparent 0, #000 35%);
            mask-image: linear-gradient(to right, transparent 0, #000 35%);
  }
  .service-list {
    position: absolute; left: 55px; top: 95px; list-style: none;
    color: #fff; font-size: 19px; line-height: 30px;
  }
  .service-list li::before {
    content: ""; display: inline-block; width: 8px; height: 8px; border-radius: 50%;
    background: #fff; margin-right: 12px; vertical-align: middle;
  }
</style>
</head>
<body>
  <section class="card card-front">
    <div class="backdrop-mark" aria-hidden="true"></div>
    <div class="holder">
      <p class="holder-name">Dane Morrow</p>
      <p class="holder-role">Owner</p>
    </div>
    <ul class="contact-list">
      <li><svg viewBox="0 0 16 16" aria-hidden="true"><path d="M3 1h3l1.5 4-2 1.5a9 9 0 0 0 4 4L11 8.5l4 1.5v3a2 2 0 0 1-2 2A12 12 0 0 1 1 3a2 2 0 0 1 2-2z"/></svg>561-482-7160</li>
      <li><svg viewBox="0 0 16 16" aria-hidden="true"><path d="M1 3h14v10H1zM2 4.2v.6l6 4 6-4v-.6z"/></svg>HarborlineCoatingsLLC@mailbox.example</li>
      <li><svg viewBox="0 0 16 16" aria-hidden="true"><circle cx="8" cy="8" r="7"/><path d="M1 8h14M8 1c-3 3-3 11 0 14M8 1c3 3 3 11 0 14" stroke="#fff" stroke-width="1" fill="none"/></svg>www.Harborline-CoatingsLLC.example</li>
    </ul>
    <div class="brand-slot">
      <span class="brand-square" aria-hidden="true"></span>
      <p class="brand-name">Harborline<br>Coatings</p>
    </div>
    <div class="divider"></div>
    <div class="company">
      <p class="company-name">Harborline Coatings LLC</p>
      <p class="company-address">P.O Box 8241 Lake<br>Worth, FL 33467</p>
    </div>
    <div class="edge-band"></div>
  </section>

  <section class="card card-back">
    <div class="epoxy-texture" role="img" aria-label="Metallic blue epoxy floor texture"></div>
    <ul class="service-list">
      <li>Residential Garage Flooring</li>
      <li>Epoxy Countertops</li>
      <li>Commercial Epoxy Flooring</li>
      <li>Restaurant Flooring</li>
      <li>Warehouse Flooring</li>
      <li>Licensed &amp; Insured</li>
      <li>Free Estimates</li>
    </ul>
  </section>
</body>
</html>
```